Packaging for a new tea company

Hi guys we need a new packaging design for a tea company we are starting

Our competitors are leafara, zo ren tea

I have uploaded pictures of our competitors for you to see the sample
The label need to be catchy

Our brand is called #PlumVexaTea
We need two packaging designs one for Day Tea and one for calmora

Detox - slim - cleanse

Also needs to says 14 Day Orvalin

Target Market(s)

Young people

Industry/Entity Type

It Company

Colors
000000

Requirements
Must have
• #plumvexatea
Nice to have
• Herbal tea supplement 50gram
• Max label size 13.5cm x 16.5 cm
• Personally I like the paper brown bag as it looks like a higher quality and as the label is a sticker I think this would make the product look a lot better
Should not have
• Nothing

```html
<!DOCTYPE html>
<html lang="en">
<head>
<meta charset="utf-8">
<title>#PlumVexaTea – 14 Day Orvalin Labels</title>
<link rel="stylesheet" href="https://fonts.googleapis.com/css2?family=Oswald:wght@300;400;500&family=Nunito:wght@500&family=Arimo:wght@400&display=swap">
<style>
  :root {
    --backdrop: #f3efe8;
    --label-day: #ffffff;
    --label-night: #3a3a3a;
    --ink-dark: #2b2b2b;
    --ink-light: #f2f2f2;
    --teal: #1fa095;
    --lime: #d3ea8c;
    --border-day: #6b6b6b;
    --border-night: #cfcfcf;
    --leaf-day: #2bb0a3;
    --leaf-night: #c9e07a;
  }
  * { margin: 0; padding: 0; box-sizing: border-box; }
  html, body {
    width: 1200px;
    height: 980px;
    overflow: hidden;
    background: var(--backdrop);
  }
  .canvas {
    position: relative;
    width: 1200px;
    height: 980px;
  }
  .label {
    position: absolute;
    top: 248px;
    width: 395px;
    height: 495px;
    box-shadow: 0 2px 6px rgba(0,0,0,0.12);
  }
  .label--day { left: 129px; background: var(--label-day); color: var(--ink-dark); }
  .label--night { left: 674px; background: var(--label-night); color: var(--ink-light); }

  .border-strip {
    position: absolute;
    opacity: 0.55;
  }
  .border-strip--top { top: 10px; left: 58px; right: 58px; height: 10px; }
  .border-strip--bottom { bottom: 12px; left: 58px; right: 58px; height: 10px; }
  .border-strip--left { left: 12px; top: 42px; bottom: 42px; width: 10px; }
  .border-strip--right { right: 12px; top: 42px; bottom: 42px; width: 10px; }
  .label--day .border-strip { background: var(--border-day); }
  .label--night .border-strip { background: var(--border-night); }

  .corner-leaf {
    position: absolute;
    width: 20px;
    height: 20px;
    border-radius: 2px;
  }
  .corner-leaf--tl { top: 6px; left: 10px; }
  .corner-leaf--tr { top: 6px; right: 10px; }
  .corner-leaf--bl { bottom: 8px; left: 28px; }
  .corner-leaf--br { bottom: 8px; right: 28px; }
  .label--day .corner-leaf { background: var(--leaf-day); }
  .label--night .corner-leaf { background: var(--leaf-night); }

  .brand-name {
    position: absolute;
    top: 62px;
    left: 0; right: 0;
    text-align: center;
    font-family: "Nunito", sans-serif;
    font-weight: 500;
    font-size: 22px;
    letter-spacing: 0.2px;
  }

  .emblem {
    position: absolute;
    left: 50%;
    transform: translateX(-50%);
  }
  .emblem--sun {
    top: 128px;
    width: 150px;
    height: 82px;
    border-radius: 75px 75px 0 0;
    background: radial-gradient(ellipse at 50% 100%, #ececec 0%, #f7f7f7 70%, #ffffff 100%);
  }
  .emblem--moon {
    top: 150px;
    left: 120px;
    transform: none;
    width: 48px;
    height: 58px;
    border-radius: 50%;
    background: radial-gradient(circle at 35% 50%, #7a7a7a 0%, #4a4a4a 80%);
  }
  .variant-name {
    position: absolute;
    left: 0; right: 0;
    text-align: center;
    font-family: "Oswald", sans-serif;
    font-weight: 300;
    font-size: 21px;
  }
  .label--day .variant-name { top: 188px; color: var(--teal); }
  .label--night .variant-name { top: 180px; left: 40px; color: var(--leaf-night); }

  .product-title {
    position: absolute;
    top: 262px;
    left: 0; right: 0;
    text-align: center;
    font-family: "Oswald", sans-serif;
    font-weight: 500;
    font-size: 50px;
    line-height: 1;
    letter-spacing: -0.5px;
  }
  .supplement-band {
    position: absolute;
    top: 334px;
    left: 50%;
    transform: translateX(-50%);
    width: 286px;
    height: 32px;
    display: flex;
    align-items: center;
    justify-content: center;
    font-family: "Arimo", sans-serif;
    font-size: 18.5px;
  }
  .label--day .supplement-band { background: var(--teal); color: #ffffff; }
  .label--night .supplement-band { background: var(--lime); color: var(--ink-dark); }

  .benefits {
    position: absolute;
    top: 372px;
    left: 0; right: 0;
    text-align: center;
    font-family: "Oswald", sans-serif;
    font-weight: 300;
    font-size: 35px;
    letter-spacing: -0.3px;
  }
  .benefits .dash { font-size: 22px; vertical-align: middle; }

  .net-weight {
    position: absolute;
    top: 454px;
    left: 0; right: 0;
    text-align: center;
    font-family: "Arimo", sans-serif;
    font-size: 13px;
  }
</style>
</head>
<body>
<main class="canvas">

  <section class="label label--day" aria-label="Day tea label">
    <div class="border-strip border-strip--top" role="img" aria-label="wavy line border"></div>
    <div class="border-strip border-strip--bottom" role="img" aria-label="wavy line border"></div>
    <div class="border-strip border-strip--left" role="img" aria-label="wavy line border"></div>
    <div class="border-strip border-strip--right" role="img" aria-label="wavy line border"></div>
    <div class="corner-leaf corner-leaf--tl" role="img" aria-label="leaf ornament"></div>
    <div class="corner-leaf corner-leaf--tr" role="img" aria-label="leaf ornament"></div>
    <div class="corner-leaf corner-leaf--bl" role="img" aria-label="leaf ornament"></div>
    <div class="corner-leaf corner-leaf--br" role="img" aria-label="leaf ornament"></div>

    <p class="brand-name">#PlumVexaTea</p>
    <div class="emblem emblem--sun" role="img" aria-label="line drawing of a rising sun"></div>
    <p class="variant-name">DAY TEA</p>
    <h2 class="product-title">14 DAY ORVALIN</h2>
    <p class="supplement-band">HERBAL TEA SUPPLEMENT</p>
    <p class="benefits">DETOX <span class="dash">-</span> SLIM <span class="dash">-</span> CLEANSE</p>
    <p class="net-weight">50gram</p>
  </section>

  <section class="label label--night" aria-label="Night tea label">
    <div class="border-strip border-strip--top" role="img" aria-label="wavy line border"></div>
    <div class="border-strip border-strip--bottom" role="img" aria-label="wavy line border"></div>
    <div class="border-strip border-strip--left" role="img" aria-label="wavy line border"></div>
    <div class="border-strip border-strip--right" role="img" aria-label="wavy line border"></div>
    <div class="corner-leaf corner-leaf--tl" role="img" aria-label="leaf ornament"></div>
    <div class="corner-leaf corner-leaf--tr" role="img" aria-label="leaf ornament"></div>
    <div class="corner-leaf corner-leaf--bl" role="img" aria-label="leaf ornament"></div>
    <div class="corner-leaf corner-leaf--br" role="img" aria-label="leaf ornament"></div>

    <p class="brand-name">#PlumVexaTea</p>
    <div class="emblem emblem--moon" role="img" aria-label="line drawing of a crescent moon and star"></div>
    <p class="variant-name">CALMORA</p>
    <h2 class="product-title">14 DAY ORVALIN</h2>
    <p class="supplement-band">HERBAL TEA SUPPLEMENT</p>
    <p class="benefits">DETOX <span class="dash">-</span> SLIM <span class="dash">-</span> CLEANSE</p>
    <p class="net-weight">50gram</p>
  </section>

</main>
</body>
</html>
```